New Website for ReBranded Company - CrewBeacon

We have a successful company and website currently but it is a little dated. We have re-branded the company from Harbor Signal Networks to CrewBeacon and have a new logo for the new name. We are looking to build a newer fresher website with the new name. I will need a concept of the home page and one inside page. You can see our current site at https://www.harborsignalnetworks.example and the new site will be https://www.crewbeacon.example .

I also really like the https://www.pathlantern.example/ website. I like ledgerkite.example website. I like the https://skillorbit.example/ website.

See the attached document for layout and some text to use. Use the pictures I attached as opposed to pictures from the old site as much as you can.

Target Market(s)

Business

Industry/Entity Type

Software Service

Number of Pages Required

2 page

Font styles to use
Sans Serif

Requirements
Must have
• Use the colors from my logo. Professional but modern. We want people to feel like our product makes their staff feel safer at work.
Should not have
• Don't use any red or orange (no stop colors).

```html
<!DOCTYPE html>
<html lang="en">
<head>
<meta charset="utf-8">
<title>CrewBeacon – Electronic Panic Button</title>
<link rel="stylesheet" href="https://fonts.googleapis.com/css2?family=Poppins:wght@300;400;500;600;700;800&display=swap">
<style>
:root{
  --blue:#3b8fd1;
  --blue-dark:#2f7dbd;
  --green:#7cc142;
  --ink:#232323;
  --muted:#6c6c6c;
  --tint:#f2f6fb;
  --white:#ffffff;
  --line:#e9eef3;
}
*{margin:0;padding:0;box-sizing:border-box}
html,body{width:1200px;height:5000px;overflow:hidden}
body{position:relative;background:var(--white);font-family:'Poppins',sans-serif;color:var(--ink)}
.abs{position:absolute}
a{color:inherit;text-decoration:none}

/* header */
.site-header{left:0;top:0;width:1200px;height:90px;background:var(--white)}
.brand{display:flex;align-items:center;gap:8px;font-weight:600;color:var(--blue)}
.brand-dot{width:26px;height:26px;border-radius:50%;background:var(--blue)}
.site-header .brand{position:absolute;left:126px;top:30px;font-size:18px}
.nav{position:absolute;left:584px;top:36px;display:flex;gap:58px;font-size:12px;font-weight:500}
.nav .active{color:var(--green);border-bottom:2px solid var(--green);padding-bottom:8px}
.btn{display:inline-flex;align-items:center;justify-content:space-between;background:var(--blue);color:var(--white);font-size:11px;font-weight:600;text-transform:uppercase;border-radius:22px;letter-spacing:.2px}
.header-cta{position:absolute;left:928px;top:25px;width:146px;height:42px;justify-content:center}
.btn-arrow{width:240px;height:42px;padding:0 26px 0 20px}
.btn-arrow svg{width:10px;height:14px}

/* hero */
.hero{left:0;top:90px;width:1200px;height:562px;background:linear-gradient(120deg,#8f8f8f,#6d6c6a 45%,#4f4c49)}
.hero-title{left:0;top:260px;width:1200px;text-align:center;color:var(--white);font-size:40px;font-weight:700;line-height:52px;text-transform:uppercase}
.hero-sub{left:0;top:383px;width:1200px;text-align:center;color:var(--green);font-size:24px;font-weight:500}
.hero .btn,.hero-btn{left:479px;top:462px}

/* feature cards */
.feature{width:300px;height:230px;background:var(--white);box-shadow:0 10px 30px rgba(20,40,70,.08);text-align:center;padding-top:20px}
.feature svg{width:46px;height:54px;margin:0 auto 30px;display:block}
.feature p{font-size:15px;font-weight:600;line-height:25px;padding:0 34px}

/* employees band */
.band{left:0;top:1109px;width:1200px;height:557px;background:var(--tint)}
.band-photo{left:560px;top:1109px;width:640px;height:557px;background:linear-gradient(135deg,#f1f3f5 0%,#dfe1e2 55%,#8f8a55 100%)}
.band-title{left:126px;top:1245px;font-size:27px;font-weight:700;line-height:54px;text-transform:uppercase}
.rule{height:3px;background:var(--blue)}
.band-copy{left:126px;top:1366px;color:var(--green);font-size:20px;font-weight:500;line-height:33px}

/* section titles */
.section-title{left:0;width:1200px;text-align:center;font-size:24px;font-weight:700}
.section-title span{display:inline-block;padding-bottom:14px;border-bottom:3px solid var(--blue)}
.upper{text-transform:uppercase}

/* why cards */
.why{width:300px;height:262px;border:2px solid var(--line);border-radius:26px;background:var(--white);text-align:center;padding:36px 30px 0}
.why h3{font-size:15px;font-weight:600;line-height:25px;text-transform:uppercase}
.why hr{width:70px;border:0;height:3px;background:var(--blue);margin:14px auto 30px}
.why p{font-size:12px;color:var(--muted);line-height:21px}
.why.is-featured{background:var(--blue);border-color:var(--blue);color:var(--white)}
.why.is-featured hr{background:var(--white)}
.why.is-featured p{color:#e3effa}

/* safety */
.safety-bg{left:126px;top:2320px;width:1074px;height:438px;background:var(--tint)}
.safety-photo{left:684px;top:2404px;width:390px;height:517px;background:linear-gradient(180deg,#2a3b4d,#1b2836 60%,#243342)}
.safety-title{left:157px;top:2412px;font-size:26px;font-weight:600;line-height:38px}
.safety-text{left:157px;top:2510px;width:420px;font-size:12px;line-height:21px;color:#444}
.btn-plain{left:157px;top:2638px;width:150px;height:40px;justify-content:center}
.safety-lead{left:157px;top:2793px;font-size:21px;line-height:38px;color:#333}
.stats{left:157px;top:2893px;font-size:25px;color:#333}
.stats b{font-weight:700}

/* plan cards */
.plan{width:300px;height:235px;border-radius:26px;background:var(--blue);color:var(--white);text-align:center;padding-top:36px}
.plan h3{font-size:16px;font-weight:600;line-height:25px;margin-bottom:30px}
.plan ul{list-style:disc;display:inline-block;text-align:left;font-size:12px;line-height:22px;padding-left:20px}
.plan p{font-size:12px;line-height:22px;padding:0 30px}

/* products */
.product{width:300px;height:239px;border-radius:26px}

/* subscribe */
.subscribe-bg{left:0;top:4220px;width:1200px;height:314px;background:linear-gradient(100deg,#3d3c3a,#6a6866 45%,#4a4845)}
.subscribe-box{left:295px;top:4241px;width:610px;height:266px;background:rgba(235,235,235,.88);text-align:center;padding-top:40px}
.subscribe-box h2{font-size:30px;font-weight:700;letter-spacing:1px;color:#3a3a3a}
.subscribe-box p{font-size:20px;color:#3a3a3a;margin-top:6px}
.sub-form{display:flex;width:516px;height:44px;margin:40px auto 0}
.sub-form span{flex:1;background:var(--white);text-align:left;padding-left:22px;line-height:44px;font-size:14px;color:#b8c8d8}
.sub-form b{width:130px;background:var(--blue);color:var(--white);font-size:14px;line-height:44px;font-weight:600;text-transform:uppercase}

/* footer */
.call{left:126px;top:4590px;width:280px;text-align:center}
.call h4{font-size:24px;font-weight:600}
.call p{font-size:26px;font-weight:700;margin-top:0}
.footer-about{left:126px;top:4672px;width:285px;font-size:14px;line-height:24px;color:#8a8a8a}
.footer-brand{left:126px;top:4820px;font-size:32px}
.footer-brand .brand-dot{width:60px;height:60px}
.footer-col{top:4682px;font-size:12px;line-height:24px;color:#8a8a8a}
.footer-col h5{font-size:11px;font-weight:700;color:#333;text-transform:uppercase;margin-bottom:20px}
.copyright{left:0;top:4950px;width:1200px;text-align:center;font-size:13px;color:#555}
</style>
</head>
<body>

<header class="site-header abs">
  <div class="brand"><span class="brand-dot"></span>CrewBeacon</div>
  <nav class="nav"><a class="active">Home</a><a>Buy Addons</a><a>Cust Login</a></nav>
  <a class="btn header-cta">Get Started</a>
</header>

<section class="hero abs" role="img" aria-label="Photo of an office team meeting with a desk phone and sticky notes on a glass wall"></section>
<h1 class="hero-title abs">Feel confident that<br>your staff is protected</h1>
<p class="hero-sub abs">Get a revolutionary new electronic panic button</p>
<a class="btn btn-arrow hero-btn abs">Ready to get started<svg viewBox="0 0 10 14"><path d="M2 1l6 6-6 6" fill="none" stroke="#fff" stroke-width="1.6"/></svg></a>

<div class="feature abs" style="left:126px;top:767px">
  <svg viewBox="0 0 46 54"><g fill="none" stroke="#4d5fb0" stroke-width="3"><rect x="16" y="3" width="14" height="11"/><rect x="3" y="38" width="14" height="11"/><rect x="29" y="38" width="14" height="11"/><rect x="16" y="22" width="14" height="8"/><path d="M23 14v8M23 30v4M10 38v-4h26v4"/></g></svg>
  <p>Problems Stopped Before They Start For Any Type Of Organization.</p>
</div>
<div class="feature abs" style="left:450px;top:767px">
  <svg viewBox="0 0 46 54"><path d="M17 6h12l-4 8h-4z" fill="#2e7d4b"/><ellipse cx="23" cy="34" rx="17" ry="18" fill="#2e7d4b"/><text x="23" y="42" text-anchor="middle" font-size="22" font-weight="700" fill="#fff" font-family="Poppins,sans-serif">$</text></svg>
  <p>Affordable Prices Starting at $18 per month. No Contracts. No Hidden Costs.</p>
</div>
<div class="feature abs" style="left:775px;top:767px">
  <svg viewBox="0 0 46 54"><g fill="none" stroke="#3aa86b" stroke-width="3"><path d="M4 18c0-8 38-8 38 0v5h-9v-5H13v5H4z"/><path d="M12 24l-5 24h32l-5-24z"/><circle cx="23" cy="36" r="6"/></g></svg>
  <p>Alerts by computer, mobile device, text, phone, email, monitoring and E911.</p>
</div>

<section class="band abs"></section>
<div class="band-photo abs" role="img" aria-label="Photo of panic button devices with cables and a lanyard on a white table"></div>
<h2 class="band-title abs">Your empoyees shouldn’t<br>feel alone when they need help</h2>
<div class="rule abs" style="left:126px;top:1356px;width:86px"></div>
<p class="band-copy abs">Does this problem make you feel frustrated<br>and anxious?<br>Put a simple solution in their hands</p>
<a class="btn btn-arrow abs" style="left:126px;top:1503px">Ready to get started<svg viewBox="0 0 10 14"><path d="M2 1l6 6-6 6" fill="none" stroke="#fff" stroke-width="1.6"/></svg></a>

<h2 class="section-title upper abs" style="top:1720px"><span>Why businesses choose us</span></h2>

<div class="why abs" style="left:126px;top:1870px"><h3>Easy to use</h3><hr><p>Press a button and let the right people know you need help and open a chat window letting everyone talk on resolving their problem.</p></div>
<div class="why is-featured abs" style="left:450px;top:1870px"><h3>Communicate the way you want</h3><hr><p>We give you lots of options:<br>* Computer *Text *Mobile *E911<br>*Email * Call Center<br>*Phone call</p></div>
<div class="why abs" style="left:775px;top:1870px"><h3>Cost effective protection</h3><hr><p>By leveraging your existing network and equipment we can lower your costs to give better options to your staff.</p></div>
<a class="btn btn-arrow abs" style="left:479px;top:2168px">Ready to get started<svg viewBox="0 0 10 14"><path d="M2 1l6 6-6 6" fill="none" stroke="#fff" stroke-width="1.6"/></svg></a>

<section class="safety-bg abs"></section>
<div class="safety-photo abs" role="img" aria-label="Photo of a person in a dark polo shirt wearing a panic button on a lanyard, shown from the chest down"></div>
<h2 class="safety-title abs">We know how scary it can feel to<br>worry about employee safety.</h2>
<p class="safety-text abs">Lorem ipsum dolor sit amet, consectetur adipiscing elit. Semper lectus lectus eget morbi lectus ut. Lorem faucibus ullamcorper in urna. Eu bibendum dolor cursus leo. Mi sollicitudin ipsum diam libero ac.</p>
<a class="btn btn-plain abs">View details</a>
<p class="safety-lead abs">That’s why we have provided a way for<br>customers to get help to staff effectively in</p>
<p class="stats abs"><b>45 States</b>&nbsp;&nbsp; covering &nbsp;&nbsp;<b>5 Countries</b></p>

<h2 class="section-title upper abs" style="top:3005px"><span>Simple start plan</span></h2>
<div class="plan abs" style="left:126px;top:3154px"><h3>Explore Your Choices</h3><ul><li>Pricing</li><li>Trial</li><li>Quote</li><li>Hardware</li></ul></div>
<div class="plan abs" style="left:450px;top:3154px"><h3>Get Setup</h3><ul><li>Input Your Alerts</li><li>Input Your Staff</li><li>Install Our Software</li></ul></div>
<div class="plan abs" style="left:775px;top:3154px"><h3>Feel Confident Your<br>Staff Is Protected</h3><p>High Five. You just too a major step to getting rid of the anxiety and frustration this gave you.</p></div>

<h2 class="section-title abs" style="top:3466px"><span>Our Products</span></h2>
<div class="product abs" style="left:126px;top:3614px;background:linear-gradient(135deg,#6c6f6a,#b9a88a 60%,#7c8f74)" role="img" aria-label="Photo of a hand pressing a panic button mounted under a counter"></div>
<div class="product abs" style="left:450px;top:3614px;background:linear-gradient(135deg,#9aa9b6,#3c4a5c 60%,#c9b99e)" role="img" aria-label="Photo of a desk phone beside a panic button"></div>
<div class="product abs" style="left:775px;top:3614px;background:linear-gradient(135deg,#e2e0da,#a9a59a 60%,#6e6a63)" role="img" aria-label="Photo of a panic button on a lanyard hanging on a wall"></div>
<div class="product abs" style="left:126px;top:3878px;background:linear-gradient(135deg,#1f2c40,#36475e 60%,#8aa0b6)" role="img" aria-label="Photo of a panic button held at a jeans pocket"></div>
<div class="product abs" style="left:450px;top:3878px;background:linear-gradient(135deg,#e9e4dc,#cfc6b8 60%,#a99f90)" role="img" aria-label="Photo of several panic button devices with cables on a table"></div>
<div class="product abs" style="left:775px;top:3878px;background:linear-gradient(135deg,#5e5a55,#2f2d2b 50%,#9d968c)" role="img" aria-label="Photo of a panic button mounted beside a door frame"></div>

<section class="subscribe-bg abs" role="img" aria-label="Blurred photo of an office desk with a phone"></section>
<div class="subscribe-box abs">
  <h2>SUBSCRIBE OUR NEWALETTER</h2>
  <p>Receive Great Deal of Northvale</p>
  <div class="sub-form"><span>Your Email Address</span><b>Subscribe</b></div>
</div>

<div class="call abs"><h4>Call Us</h4><p>1 – 800 – 555 – 0142</p></div>
<p class="footer-about abs">When employees feel alone during a threatening situation, we give them a way to let the right resources know that they need help so you can feel confident that your staff is protected.</p>
<div class="brand footer-brand abs"><span class="brand-dot"></span>CrewBeacon</div>

<div class="footer-col abs" style="left:522px"><h5>Shop</h5>Add Ons<br>Start My Demo<br>Custom Quote<br>Start Trial</div>
<div class="footer-col abs" style="left:680px"><h5>About</h5>Affiliates<br>Contact<br>Support<br>Existing Customers<br>Industries<br>Blog<br>FAQ</div>
<div class="footer-col abs" style="left:864px"><h5>Legal</h5>Privacy Policy<br>Terms of Use<br>End User License Agreement</div>

<p class="copyright abs">©CrewBeacon 2020</p>
</body>
</html>
```